Basic Commercial & Residential Real Estate Web Site

I need a basic website for a new real estate company that deals with both residential and commercial sales. It must be clean and professional. We sell homes, office buildings, farms, and ranches. It should feel crisp and clean.
I need a main page with my logo and links to commercial, residential, farm and land searches with contact data forms. Also incorporated would be a mls property search (IDX) form. I am in Northern California and the current site I posted is at www.tqvandel.com. I need the functionality of the links and the supporting pages. I do not have all the copy ready because I did not know what to expect.
Updates

Project Deadline Extended
Reason: I apologize, I am extremely busy and you all need more data to do a good job. All the designs are great so far and it is extremely difficult to choose at this point. I haven't given you enough data. I haver now uploaded some relevent photos (not very good) and edited the brief. I am looking for what I call the Landing or main page with some functionality built in to other pages which I also need. Example if you click on "Commercial" it should go to a page that discusses our commercial dept.......

I would like to thank all the designers for all their hard work and efforts, I wish I could reward you all.

Thanks again for your creative and professional designs.

Gareth

Target Market(s)

Corporate Execs for the Commercial Buildings
Homeowners/Families for the Homes and Farms
Upper end people for the land to build estates

Industry/Entity Type

Real Estate

Font styles to use
Sans Serif

Requirements
Must have
• Our Logo should be prominent, pronounced
Need contact data or button
Functional Page that links to other data pages
Must Have a "search for properties" feature
Must say "Commercial and Residential Representation"
Pictures of Commercial Building and Nice Home (Tradtional not contemporary)
Nice to have
• Individual Buttons or links to "Commercial, Residential, Farm/Ranch, Land"
Contact Data displayed
button that says "Maple Crest"-next to button is Maple Crest Logo-see www.maplecrestvale.bz
Links to "Buyers and "Sellers"
Links to Facebook, twitter,.....etc
Should not have
• 20+ story commercial buildings or ultra modern. See uploaded files of typical buildings for commercial.

```html
<!DOCTYPE html>
<html lang="en">
<head>
<meta charset="utf-8">
<title>Properties by Halden</title>
<link href="https://fonts.googleapis.com/css2?family=Open+Sans:wght@300;400;600&family=Questrial&display=swap" rel="stylesheet">
<style>
:root{
  --header-dark:#2b3340;
  --accent:#3aa6d9;
  --btn-top:#4fbdea;
  --btn-bottom:#2291c9;
  --text:#3a3a3a;
  --muted:#8a8a8a;
  --card-border:#dcdcdc;
  --footer:#2a2a2a;
  --footer-text:#e8e8e8;
  --footer-muted:#8c8c8c;
}
*{box-sizing:border-box;margin:0;padding:0}
html,body{width:746px;height:1200px;overflow:hidden}
body{position:relative;font-family:"Open Sans",sans-serif;color:var(--text);background:#fff}
.site-header{position:absolute;left:0;top:0;width:746px;height:86px;
  background:linear-gradient(180deg,#3c4552 0%,#262d38 60%,#1f2530 100%)}
.brand{position:absolute;left:54px;top:18px;color:#fff;font-family:"Questrial",sans-serif;line-height:1}
.brand .small{display:block;font-size:12px;letter-spacing:1px;padding-left:44px}
.brand .big{display:block;font-size:38px;letter-spacing:2px;margin-top:2px}
.search{position:absolute;left:460px;top:17px;width:152px;height:17px;border-radius:9px;
  background:#1c2129;border:1px solid #4a525e;font-size:7px;font-style:italic;color:#9aa0a8;padding:3px 8px}
.search svg{position:absolute;right:6px;top:3px}
.social-top{position:absolute;left:632px;top:17px;display:flex;gap:6px}
.social-top span{width:16px;height:16px;border-radius:50%;background:#fff}
.main-nav{position:absolute;left:282px;top:52px;display:flex;font-size:11.5px;color:#fff}
.main-nav a{color:#fff;text-decoration:none;padding:0 12px;border-left:1px solid #6a717c;line-height:12px}
.main-nav a:first-child{border-left:0;color:var(--accent)}
.hero{position:absolute;left:0;top:86px;width:746px;height:304px;
  background:linear-gradient(180deg,#6f9cc8 0%,#b9c9d6 25%,#8a6a4e 45%,#9c7a55 65%,#5f8a35 82%,#4c7a2a 100%)}
.hero h1{position:absolute;top:108px;width:100%;text-align:center;color:#fff;font-weight:400;font-size:26px;
  font-family:"Open Sans",sans-serif;text-shadow:0 1px 3px rgba(0,0,0,.5)}
.hero h2{position:absolute;top:144px;width:100%;text-align:center;color:#fff;font-weight:400;font-size:19px;
  text-shadow:0 1px 3px rgba(0,0,0,.5)}
.dots{position:absolute;top:283px;left:348px;display:flex;gap:4px}
.dots span{width:9px;height:9px;border-radius:50%;background:rgba(255,255,255,.45)}
.dots span:first-child{background:#fff}
.welcome{position:absolute;top:418px;left:70px;width:606px;text-align:center}
.welcome h2{font-family:"Questrial",sans-serif;font-weight:400;font-size:22px;color:#222}
.welcome p{font-size:8.6px;line-height:15px;color:#6a6a6a;margin-top:6px}
.cards{position:absolute;top:518px;left:63px;display:flex;gap:12px}
.card{width:200px;height:200px;border:1px solid var(--card-border);background:#fff;text-align:center}
.card .photo{height:91px}
.card h3{font-weight:400;font-size:15px;margin-top:11px;color:#333}
.card p{font-size:7.8px;line-height:12.5px;color:var(--muted);padding:0 16px;margin-top:3px}
.btn{display:inline-block;margin-top:7px;width:71px;height:20px;line-height:20px;border-radius:2px;font-size:7.8px;
  color:#fff;background:linear-gradient(var(--btn-top),var(--btn-bottom))}
.about{position:absolute;left:52px;top:768px;width:390px}
.about h2{font-weight:300;font-size:19px;color:#333}
.about .lead{font-size:9.6px;line-height:14px;color:#555;margin-top:6px}
.about p{font-size:8px;line-height:13.6px;color:#666;margin-top:6px}
.gallery{position:absolute;left:465px;top:760px;width:230px;height:181px;border:1px solid #d8d8d8;
  background:linear-gradient(#fff,#f2f2f2)}
.gallery h2{font-weight:400;font-size:15px;color:var(--accent);margin:14px 0 0 17px}
.thumbs{display:grid;grid-template-columns:repeat(3,58px);gap:12px 12px;margin:10px 0 0 17px}
.thumbs div{height:54px;border:3px solid #fff;box-shadow:0 0 2px rgba(0,0,0,.3)}
.stripe{position:absolute;left:0;top:982px;width:746px;height:5px;
  background:repeating-linear-gradient(90deg,#bbb 0 2px,#eee 2px 4px)}
.site-footer{position:absolute;left:0;top:987px;width:746px;height:213px;background:var(--footer);color:var(--footer-text)}
.col{position:absolute;top:26px}
.col h4{font-weight:400;font-size:12.5px;margin-bottom:6px}
.col li{list-style:none;font-size:8px;line-height:15.8px}
.col .contact{font-size:8px;line-height:13.6px}
.col .phone{font-size:10.4px;line-height:17px}
.footer-rule{position:absolute;left:58px;top:161px;width:637px;height:1px;background:#3c3c3c}
.copyright{position:absolute;left:59px;top:174px;font-size:7.6px;color:var(--footer-muted)}
.social-bottom{position:absolute;left:602px;top:176px;display:flex;gap:6px}
.social-bottom span{width:15px;height:15px;border-radius:2px}
</style>
</head>
<body>
<header class="site-header">
  <div class="brand"><span class="small">PROPERTIES BY</span><span class="big">HALDEN</span></div>
  <div class="search">Search here..
    <svg width="9" height="9" viewBox="0 0 10 10"><circle cx="4" cy="4" r="3" fill="none" stroke="#9aa0a8" stroke-width="1.2"/><line x1="6.2" y1="6.2" x2="9" y2="9" stroke="#9aa0a8" stroke-width="1.2"/></svg>
  </div>
  <div class="social-top"><span></span><span></span><span></span></div>
  <nav class="main-nav"><a>HOME</a><a>COMMERCIAL</a><a>RESIDENTIAL</a><a>FARM</a><a>LAND</a><a>CONTACT</a></nav>
</header>

<section class="hero" role="img" aria-label="Traditional brick country house with tiled roof under a blue sky, lawn in front">
  <h1>BUYER AND SELLER REPRESENTATION</h1>
  <h2>COMMERCIAL &amp; RESIDENTIAL</h2>
  <div class="dots"><span></span><span></span><span></span><span></span></div>
</section>

<section class="welcome">
  <h2>Welcome to Properties by Halden homepage</h2>
  <p>Phasellus felis dolor scelerisque a tempus eget lobortis id libero Aliquam nec erat at purus cursus interdum Vestibulum ligula augue bibendum accumsan vestibulum ut commodo a mi Morbi ornare gravida elit Integer congue augue et malesuada iaculis ipsum dui aliquet felis at cursus magna nisl nec elit Vestibulum gravida Praesent elementum elit at tellus Malesuada nec ultricies sit amet porttitor</p>
</section>

<section class="cards">
  <article class="card">
    <div class="photo" role="img" aria-label="Bright luxury home kitchen interior" style="background:linear-gradient(135deg,#e8e4dd,#9c958b 60%,#4a443e)"></div>
    <h3>Luxury Home</h3>
    <p>Mauris neque metus malesuada nec ultri-cies sit amet porttitor mattis enim. In massa libero interdum nec</p>
    <span class="btn">VIEW MORE</span>
  </article>
  <article class="card">
    <div class="photo" role="img" aria-label="Glass office buildings against a blue sky" style="background:linear-gradient(135deg,#9cc4e6,#2f6d9e 55%,#173a5c)"></div>
    <h3>Office Buildings</h3>
    <p>Mauris neque metus malesuada nec ultri-cies sit amet porttitor mattis enim. In massa libero interdum nec</p>
    <span class="btn">VIEW MORE</span>
  </article>
  <article class="card">
    <div class="photo" role="img" aria-label="Rolling farmland with trees and hills" style="background:linear-gradient(180deg,#c9d3d6,#8c8a55 35%,#b58a4a 70%,#c99a56)"></div>
    <h3>Farms &amp; Ranches</h3>
    <p>Mauris neque metus malesuada nec ultri-cies sit amet porttitor mattis enim. In massa libero interdum nec</p>
    <span class="btn">VIEW MORE</span>
  </article>
</section>

<section class="about">
  <h2>About Our Company</h2>
  <p class="lead">Pellentesque faucibus Ut accumsan ultricies elit Maecenas at justo id velit placerat mo-lestie Donec dictum lectus non odio Cras a ante vitae enim iaculis aliquam</p>
  <p>Duis tincidunt lectus quis dui viverra vestibulum. Suspendisse vulputate aliquam dui. Nulla elemen-tum dui ut augue. Aliquam vehicula mi at mauris. Maecenas placerat, nisl at consequat rhoncus, sem nunc gravida justo, quis eleifend arcu velit quis lacus.</p>
  <p>Aliquam nec erat at purus cursus interdum Vestibulum ligula augue bibendum accumsan vestibulum ut commodo a mi Morbi ornare gravida elit Integer congue augue et malesuada iaculis ipsum dui aliquet felis at cursus , imperdiet vitae, tellus.</p>
</section>

<aside class="gallery">
  <h2>OUR GALLERY</h2>
  <div class="thumbs">
    <div role="img" aria-label="Farmhouse in a wheat field" style="background:linear-gradient(180deg,#5a9ad6 40%,#c99a4a 60%)"></div>
    <div role="img" aria-label="Office building" style="background:linear-gradient(180deg,#b7c9db,#7c8c99)"></div>
    <div role="img" aria-label="Home interior living room" style="background:linear-gradient(135deg,#d9c9a8,#8a6a44)"></div>
    <div role="img" aria-label="Modern interior with sea view" style="background:linear-gradient(180deg,#7fb6d9,#3e6f8c 60%,#d8d8d8)"></div>
    <div role="img" aria-label="Two storey family house" style="background:linear-gradient(180deg,#c9d3dc,#7a7a78 60%,#4f6a3a)"></div>
    <div role="img" aria-label="Suburban house with lawn" style="background:linear-gradient(180deg,#4c86c6 40%,#7a5a48 65%,#4f7a34)"></div>
  </div>
</aside>

<div class="stripe"></div>
<footer class="site-footer">
  <div class="col" style="left:65px"><h4>About us</h4><ul><li>About Us</li><li>Commercial</li><li>Residential</li><li>Farms</li><li>Land</li></ul></div>
  <div class="col" style="left:179px"><h4>Featured</h4><ul><li>Buying</li><li>Selling</li><li>Leasing</li><li>Investment</li><li>Service Area</li></ul></div>
  <div class="col" style="left:297px"><h4>Sublinks</h4><ul><li>Lenders</li><li>Architects</li><li>Builders</li><li>Other Services</li><li>Local Links</li></ul></div>
  <div class="col" style="left:417px"><h4>Support</h4><ul><li>Support</li><li>Testimonials</li><li>Contact Us</li></ul></div>
  <div class="col" style="left:534px"><h4>Contact Information</h4>
    <p class="contact">20440 Maple Crest Drive<br>Birchfield, CA 96120<br>BRE#02817346</p>
    <p class="phone">530.555.0142<br>707.555.0187</p>
  </div>
  <div class="footer-rule"></div>
  <p class="copyright">Copyright © 2014 Company Name.&nbsp; All right reseved</p>
  <div class="social-bottom">
    <span style="background:#3b5a98"></span><span style="background:#3fb0e0"></span><span style="background:#1d79b3"></span><span style="background:#f08a1f"></span>
  </div>
</footer>
</body>
</html>
```